E-brochure to promote our franchise opportunity to potential finance professionals

We need my words putting into a brochure, setting out, adding photographs and images ready for publication as a .pdf
The brochure needs to be readable as a pdf, I have no plans to publish on paper so should be well structured for a screen or tablet - easy navigation and a positive and striking visual feel

Target Market(s)

Potential business owners in business finance arranging - existing business bankers leaving their post, mortgage brokers expanding their business or existing commercial finance brokers looking for a means to expand their reach and have the help and support of a franchisor organisation

Industry/Entity Type

Finance

Font styles to use
Serif
Script

Colors
0555a3
eaf2ce

Requirements
Must have
• The project must have a professional but still accessible feel, we are not aiming to be a "corporate" like a merchant bank, our clients are ordinary small business owners, like you, so we need to speak their language. Our business is about the people we help, the dreams that come true because we help them and the wealth we create for them.
Nice to have
• Great artwork, interesting photographs, a compelling front cover page, pages which are easily readable, not too text heavy but getting the point across
Should not have
• Should not be boring - over corporate or too frivolous

```html
<!DOCTYPE html>
<html lang="en">
<head>
<meta charset="utf-8">
<title>Harlow Capital – Franchise Opportunity</title>
<link href="https://fonts.googleapis.com/css2?family=Cinzel:wght@400;600&family=Cormorant+Garamond:wght@400&family=Lato:ital,wght@0,400;0,700;1,700&display=swap" rel="stylesheet">
<style>
  :root {
    --navy: #0b3058;
    --navy-soft: #4f6f8f;
    --mist: #b7c5d2;
    --paper: #ffffff;
    --ink: #2b2b2b;
    --muted: #9a9a9a;
    --backdrop: #dcdcdc;
  }
  * { margin: 0; padding: 0; box-sizing: border-box; }
  html, body { width: 1200px; height: 1200px; overflow: hidden; background: var(--backdrop); }
  .spread { position: relative; width: 1200px; height: 1200px; }
  .page { position: absolute; background: var(--paper); overflow: hidden; box-shadow: 0 4px 14px rgba(0,0,0,.18); }
  .page svg.page-art { position: absolute; inset: 0; }

  /* Cover */
  .cover { left: 60px; top: 82px; width: 506px; height: 711px; }
  .brand { position: absolute; left: 300px; top: 36px; width: 206px; }
  .brand-name { font-family: "Cinzel", serif; font-weight: 400; font-size: 21px; color: var(--navy); letter-spacing: .5px; white-space: nowrap; }
  .brand-tagline { font-family: "Cormorant Garamond", serif; font-size: 11px; color: var(--muted); margin-top: 3px; white-space: nowrap; }
  .brand-rule { height: 2px; background: var(--navy); margin-top: 3px; }
  .cover-title { position: absolute; left: 264px; top: 600px; }
  .cover-title h1 { font-family: "Cinzel", serif; font-weight: 400; font-size: 25px; color: var(--navy); letter-spacing: .5px; line-height: 1; white-space: nowrap; }
  .cover-title h2 { font-family: "Cinzel", serif; font-weight: 400; font-size: 13px; color: var(--ink); letter-spacing: .6px; margin-top: 6px; }
  .cover-meta { font-family: "Lato", sans-serif; font-size: 8.6px; color: #555; line-height: 1.25; margin-top: 6px; padding-left: 2px; }

  /* Back page */
  .joining { left: 642px; top: 290px; width: 510px; height: 714px; }
  .joining-copy { position: absolute; right: 172px; top: 542px; width: 320px; text-align: right; }
  .joining-copy .kicker { font-family: "Cinzel", serif; font-size: 19px; color: var(--navy); letter-spacing: .6px; line-height: 1; }
  .joining-copy .headline { font-family: "Cinzel", serif; font-weight: 600; font-size: 36px; color: var(--navy); line-height: 1.05; letter-spacing: .5px; }
  .joining-copy p { font-family: "Lato", sans-serif; font-size: 9.3px; color: var(--ink); line-height: 1.25; margin-top: 6px; }
  .joining-copy .figure { font-weight: 700; font-size: 11.5px; }
  .joining-copy .brand-ref { color: var(--navy); font-weight: 700; }
  .joining-copy em { font-weight: 700; }
</style>
</head>
<body>
<main class="spread">

  <section class="page cover">
    <svg class="page-art" width="506" height="711" viewBox="0 0 506 711">
      <defs>
        <linearGradient id="kitchen-tone" x1="0" y1="0" x2="1" y2="1">
          <stop offset="0" stop-color="#d8c2ad"/>
          <stop offset=".5" stop-color="#a47d60"/>
          <stop offset="1" stop-color="#6e4a33"/>
        </linearGradient>
        <linearGradient id="meeting-tone" x1="0" y1="0" x2="1" y2="1">
          <stop offset="0" stop-color="#f1f3f4"/>
          <stop offset=".55" stop-color="#d9d6d0"/>
          <stop offset="1" stop-color="#b8a48c"/>
        </linearGradient>
      </defs>
      <rect class="side-band" x="0" y="0" width="205" height="711" fill="var(--navy)"/>
      <polygon role="img" aria-label="Photo: chef plating dishes in a restaurant kitchen" points="145.6,44 236,97.6 236,201.6 145.6,256 48,201.6 48,97.6" fill="url(#kitchen-tone)" stroke="#fff" stroke-width="3"/>
      <polygon role="img" aria-label="Photo: three colleagues smiling in a bright office meeting" points="226.4,231.2 378.4,317.6 378.4,492 226.4,581.6 72,492 72,317.6" fill="url(#meeting-tone)"/>
      <polygon class="accent-hex" points="340,175.2 414.4,217.6 414.4,301.6 340,345.6 264.8,301.6 264.8,217.6" fill="var(--mist)" opacity=".92"/>
      <polygon class="accent-hex" points="150.4,499.2 225.6,540 225.6,628 150.4,669.6 76,628 76,540" fill="var(--navy-soft)" opacity=".75"/>
    </svg>

    <div class="brand">
      <div class="brand-name">Harlow Capital</div>
      <div class="brand-tagline">Backing small firms and their investors</div>
      <div class="brand-rule"></div>
    </div>

    <div class="cover-title">
      <h1>HARLOW CAPITAL</h1>
      <h2>Franchise Opportunity</h2>
      <div class="cover-meta">
        Prepared for:<br>
        Prepared by: Mark Ellison, Principal.<br>
        3 October 2016
      </div>
    </div>
  </section>

  <section class="page joining">
    <svg class="page-art" width="510" height="714" viewBox="0 0 510 714">
      <defs>
        <linearGradient id="savings-tone" x1="0" y1="0" x2="1" y2="1">
          <stop offset="0" stop-color="#c9c290"/>
          <stop offset=".45" stop-color="#e6e2c8"/>
          <stop offset="1" stop-color="#c7ccd4"/>
        </linearGradient>
        <linearGradient id="sunset-tone" x1="0" y1="0" x2="1" y2="1">
          <stop offset="0" stop-color="#8d7a4e"/>
          <stop offset=".5" stop-color="#d9b56c"/>
          <stop offset="1" stop-color="#3d3322"/>
        </linearGradient>
      </defs>
      <rect class="side-band" x="351" y="0" width="159" height="714" fill="var(--navy)"/>
      <polygon role="img" aria-label="Photo: rising stacks of coins beside an alarm clock" points="265.6,18.4 401.6,96.8 401.6,254.4 265.6,330.4 129.6,254.4 129.6,96.8" fill="url(#savings-tone)"/>
      <polygon role="img" aria-label="Photo: coin stacks against a golden sunset" points="343.2,304.8 434.4,356.8 434.4,462.4 343.2,512.8 251.2,462.4 251.2,356.8" fill="url(#sunset-tone)"/>
    </svg>

    <div class="joining-copy">
      <div class="kicker">JOINING HARLOW.</div>
      <div class="headline">CAPITAL</div>
      <p>With a minimum investment of only <span class="figure">£8,500</span> the <span class="brand-ref">HARLOW CAPITAL</span> offers<br>
      fantastic value for money and the opportunity to <em>join a growing, professional<br>
      business and to secure your future income.</em></p>
      <p>Projected income <span class="figure">£75,000</span> in year one, growing there after.</p>
      <p>To apply please make contact by phone in the first instance, this<br>
      will then be followed up with a business plan and a full interview.</p>
    </div>
  </section>

</main>
</body>
</html>
```